I need a website for my moving company Bolt Hauling LLC. I would like the following text included in my website. I have purchased the domain bolthaulingcrew.example from siteburrow.example. I am not familiar with SEO or other techniques that help my page on search engines but would like the website to be optimized for Findora search engine. I have attached our logo below and would like it to be used in the design. The colors in the logo can be used also in the design.
Home/About Us
At Bolt Hauling LLC, we know moving. It can be difficult, stressful, and a real pain in the backside. But it doesn’t have to be! When you partner with Bolt, you get the benefits of a professional moving team that is licensed and insured for your protection along with years of experience and a dedication to providing the highest quality service, each and every time.
Our Services
We do a wide variety of local moves, including apartments, single-family homes, retirement communities, dorms, condos, and many more! Our movers are trained to protect your belongings and your home – all pieces of furniture are padded and stretch wrapped free of charge, ensuring your items and home are damage-free at the end of your move. Having added stress about packing up your home prior to moving? We’ve got you covered with our full service packing and unpacking services, too.
What You Get
When you partner with BOLT, you’ll get the best service in the industry, as well as:
* The Use of Packing & Moving Materials: The hourly rate includes the use of our dollies, ratchet straps, pads, moving tools, and property protection like floor mats, door-jamb protectors, stairwell protectors, and plenty of muscle!
• Trained, Licensed, and Insured Movers: All of our movers are highly trained to provide you with the best service, and to ensure the protection of you and your items.
• Professional: Honest, Uniformed, Nice, Knowledgeable Service is what you’ll get with every member of our moving teams.
• Custom Service for Every Move: Every move is as unique as the person or business moving. Our training and equipment allows us to customize every project to ensure the very best for every client.
Target Market(s)
Home and Business movers
Industry/Entity Type
Moving Company
Colors
Designer to choose colors to be used in the design.
Requirements
Must have
- 2 sides
Nice to have
- Colorful design with logo included.
Should not have
- animated characters

```html
<!DOCTYPE html>
<html lang="en">
<head>
<meta charset="utf-8">
<title>Bolt Hauling LLC – Maple Grove, MS</title>
<link rel="stylesheet" href="https://fonts.googleapis.com/css2?family=Bree+Serif&family=Open+Sans:wght@400;600;700&family=Roboto+Condensed:wght@700&display=swap">
<style>
:root{
  --green:#5c9d1e;
  --green-dark:#4a8416;
  --orange:#f7941d;
  --dark:#2e2e2e;
  --darker:#262626;
  --band:#ececec;
  --paper:#e9e6e1;
  --text:#3d3d3d;
  --white:#ffffff;
}
*{box-sizing:border-box;margin:0;padding:0}
html,body{width:1200px;height:3141px;overflow:hidden}
body{position:relative;font-family:"Open Sans",Arial,sans-serif;color:var(--text);background:var(--white)}
.abs{position:absolute}

/* hero */
.hero{left:0;top:0;width:1200px;height:697px;background:linear-gradient(180deg,#3d4a5c 0%,#5b6b80 45%,#2d3a4c 100%)}
.hero-photo{left:0;top:0;width:1200px;height:697px;background:radial-gradient(ellipse at 60% 45%,#8a8f96 0%,#56616f 45%,#28344a 100%);opacity:.9}
.brand{left:70px;top:30px;display:flex;align-items:center;gap:10px;color:var(--orange);font:700 22px "Open Sans",sans-serif}
.brand-dot{width:34px;height:34px;border-radius:50%;background:var(--green)}
.nav{left:350px;top:46px;display:flex;gap:42px;font:600 16px "Open Sans",sans-serif;color:var(--white);text-transform:uppercase}
.nav-call{left:890px;top:42px;display:flex;align-items:center;gap:8px;color:var(--orange);font:400 19px "Open Sans",sans-serif}
.nav-call strong{font-weight:600}
.hero-title{left:0;top:240px;width:1200px;text-align:center;color:var(--white);font:400 70px/1.05 "Bree Serif",serif}
.btn{display:inline-block;background:var(--orange);color:var(--white);border-radius:24px;font:600 16px "Open Sans",sans-serif;text-transform:uppercase;text-align:center}
.hero-btn{left:520px;top:418px;width:160px;height:44px;line-height:44px;border:2px solid rgba(255,255,255,.6)}
.hero-phone{left:0;top:494px;width:1200px;text-align:center;color:var(--white);font:600 22px "Open Sans",sans-serif}

/* intro band */
.intro{left:0;top:697px;width:1200px;height:737px;background:linear-gradient(180deg,var(--band) 0,var(--white) 260px)}
.card-photo{height:341px}
.card-photo.about{left:73px;top:754px;width:509px;background:linear-gradient(135deg,#6fa6c9,#c9a06a 70%,#e7e2d6)}
.card-photo.services{left:614px;top:754px;width:510px;background:linear-gradient(135deg,#d6cdbf,#b9a184 60%,#8ba0b3)}
.card-title{top:1058px;height:66px;width:474px;background:var(--white);padding:18px 24px;font:700 36px/1 "Roboto Condensed",sans-serif;color:var(--green);text-transform:uppercase;border-bottom:2px solid #d8d8d8}
.card-title.about{left:93px}
.card-title.services{left:634px}
.card-text{top:1150px;width:430px;font:400 14.6px/26px "Open Sans",sans-serif}
.card-text.about{left:118px}
.card-text.services{left:656px}

/* guarantee */
.guarantee-photo{left:653px;top:1434px;width:547px;height:696px;background:linear-gradient(160deg,#d9dde2 0%,#6d8fb8 55%,#2d4a86 100%)}
.guarantee{left:0;top:1434px;width:653px;height:696px;background:var(--dark)}
.guarantee-title{left:74px;top:1476px;width:520px;padding-bottom:12px;border-bottom:1px solid #555;font:700 34px/1 "Roboto Condensed",sans-serif;color:var(--green);text-transform:uppercase}
.guarantee-lead{left:74px;top:1542px;width:520px;color:var(--white);font:400 14.6px/26px "Open Sans",sans-serif}
.perk{width:250px;color:var(--white)}
.perk h3{font:600 15.5px/22px "Open Sans",sans-serif;margin-bottom:16px}
.perk p{font:400 14px/26px "Open Sans",sans-serif}
.perk-divider-v{left:316px;top:1596px;width:1px;height:484px;background:#555}
.perk-divider-h{left:74px;top:1862px;width:540px;height:1px;background:#555}

/* subscribe / book */
.subscribe{left:73px;top:2184px;width:509px;height:417px;background:var(--paper);text-align:center}
.sub-icon{left:286px;top:2207px;width:100px;height:100px;border-radius:50%;background:var(--green)}
.sub-title{left:73px;top:2326px;width:509px;text-align:center;font:700 36px/1 "Roboto Condensed",sans-serif;color:var(--green);text-transform:uppercase}
.sub-text{left:73px;top:2378px;width:509px;text-align:center;font:400 16px/25px "Open Sans",sans-serif}
.sub-input{left:101px;top:2456px;width:458px;height:48px;background:var(--white);border:1px solid #cfcfcf;padding:0 18px;line-height:46px;font:400 13px/46px "Open Sans",sans-serif;color:#777}
.sub-btn{left:101px;top:2523px;width:458px;height:50px;line-height:50px;border-radius:0;font-size:18px}
.book{left:614px;top:2184px;width:510px;height:417px;background:linear-gradient(180deg,#27364b,#3a4e6a 55%,#1f2b3c)}
.book-panel{left:740px;top:2258px;width:258px;height:186px;background:rgba(20,20,20,.72)}
.book-title{left:614px;top:2224px;width:510px;text-align:center;color:var(--white);font:400 35px/36px "Bree Serif",serif;text-transform:uppercase}
.book-sub{left:614px;top:2324px;width:510px;text-align:center;color:var(--white);font:400 24px "Open Sans",sans-serif}
.book-stat{top:2372px;width:80px;text-align:center;color:var(--white);font:400 16px "Open Sans",sans-serif}
.book-stat .ic{width:52px;height:52px;border-radius:50%;margin:0 auto 10px}
.book-btn{left:790px;top:2508px;width:158px;height:46px;line-height:46px;font-size:15px;border:2px solid rgba(255,255,255,.6)}

/* contact */
.contact{left:0;top:2660px;width:496px;height:418px;background:var(--dark)}
.map{left:496px;top:2660px;width:704px;height:418px;background:linear-gradient(135deg,#e6e6e3,#d9dbd4 60%,#cfd8e3)}
.map-btn{left:546px;top:2665px;width:164px;height:34px;background:var(--green);color:var(--white);font:600 13px/34px "Open Sans",sans-serif;text-transform:uppercase;text-align:center}
.contact-title{left:100px;top:2694px;color:var(--white);font:700 36px/1 "Roboto Condensed",sans-serif;text-transform:uppercase}
.contact-item{left:104px;width:380px;display:flex;gap:16px;color:var(--white)}
.contact-item svg{flex:0 0 28px}
.contact-item h4{font:400 17px/24px "Open Sans",sans-serif}
.contact-item p{font:400 13px/20px "Open Sans",sans-serif;color:#ddd}

.footer{left:0;top:3078px;width:1200px;height:63px;background:var(--darker)}
.footer-copy{left:72px;top:3102px;color:#ddd;font:400 13px "Open Sans",sans-serif}
.footer-social{left:1098px;top:3092px;width:30px;height:30px;border-radius:50%;background:var(--white)}
</style>
</head>
<body>

<header>
  <div class="abs hero"></div>
  <div class="abs hero-photo" role="img" aria-label="Movers in uniform carrying cardboard boxes out of a moving van"></div>
  <div class="abs brand"><span class="brand-dot"></span>Bolt Hauling</div>
  <nav class="abs nav"><span>Home</span><span>About Us</span><span>Services</span><span>FAQ</span><span>Contact Us</span></nav>
  <div class="abs nav-call">
    <svg width="20" height="20" viewBox="0 0 24 24"><path fill="var(--orange)" d="M6.6 10.8a15.1 15.1 0 0 0 6.6 6.6l2.2-2.2c.3-.3.7-.4 1-.2 1.1.4 2.3.6 3.6.6.6 0 1 .4 1 1V20c0 .6-.4 1-1 1A17 17 0 0 1 3 4c0-.6.4-1 1-1h3.5c.6 0 1 .4 1 1 0 1.3.2 2.5.6 3.6.1.3 0 .7-.2 1z"/></svg>
    Call Us: <strong>(555) 014-2737</strong>
  </div>
  <h1 class="abs hero-title">Bolt Hauling LLC<br>Maple Grove, MS</h1>
  <span class="abs btn hero-btn">Book Today</span>
  <div class="abs hero-phone">(555) 014-2737</div>
</header>

<section>
  <div class="abs intro"></div>
  <div class="abs card-photo about" role="img" aria-label="Two smiling movers unloading boxes from a van"></div>
  <div class="abs card-photo services" role="img" aria-label="Family unpacking boxes together in their new home"></div>
  <h2 class="abs card-title about">About Us</h2>
  <h2 class="abs card-title services">Our Services</h2>
  <p class="abs card-text about">At Bolt Hauling LLC, we know moving. It can be difficult, stressful, and a real pain in the backside. But it doesn’t have to be! When you partner with Bolt, you get the benefits of a professional moving team that is licensed and insured for your protection along with years of experience and a dedication to providing the highest quality service, each and every time.</p>
  <p class="abs card-text services">We do a wide variety of local moves, including apartments, single-family homes, retirement communities, dorms, condos, and many more! Our movers are trained to protect your belongings and your home – all pieces of furniture are padded and stretch wrapped free of charge, ensuring your items and home are damage-free at the end of your move. Having added stress about packing up your home prior to moving? We’ve got you covered with our full service packing and unpacking services, too.</p>
</section>

<section>
  <div class="abs guarantee-photo" role="img" aria-label="Two smiling movers in overalls standing with arms crossed in front of a white van"></div>
  <div class="abs guarantee"></div>
  <h2 class="abs guarantee-title">Our Gaurantee</h2>
  <p class="abs guarantee-lead">When you partner with BOLT, you’ll get the best service in the industry, as well as:</p>
  <div class="abs perk-divider-v"></div>
  <div class="abs perk-divider-h"></div>
  <div class="abs perk" style="left:74px;top:1604px"><h3>The Use of Packing &amp; Moving Materials:</h3><p>The hourly rate includes the use of our dollies, ratchet straps, pads, moving tools, and property protection like floor mats, door-jamb protectors, stairwell protectors, and plenty of muscle!</p></div>
  <div class="abs perk" style="left:338px;top:1604px"><h3>Trained, Licensed, and Insured Movers:</h3><p>All of our movers are highly trained to provide you with the best service, and to ensure the protection of you and your items.</p></div>
  <div class="abs perk" style="left:74px;top:1880px"><h3>Professional:</h3><p>Honest, Uniformed, Nice, Knowledgeable Service is what you’ll get with every member of our moving teams.</p></div>
  <div class="abs perk" style="left:338px;top:1880px"><h3>Custom Service for Every Move:</h3><p>Every move is as unique as the person or business moving. Our training and equipment allows us to customize every project to ensure the very best for every client.</p></div>
</section>

<section>
  <div class="abs subscribe"></div>
  <div class="abs sub-icon">
    <svg width="100" height="100" viewBox="0 0 100 100"><rect x="32" y="36" width="40" height="28" fill="none" stroke="#fff" stroke-width="3"/><path d="M32 36l20 16 20-16" fill="none" stroke="#fff" stroke-width="3"/><path d="M20 44h8M22 52h6M24 60h4" stroke="#fff" stroke-width="3"/></svg>
  </div>
  <h2 class="abs sub-title">Subscribe</h2>
  <p class="abs sub-text">Sign up to hear from us<br>about specials, packing tips, and more.</p>
  <div class="abs sub-input">Email Address</div>
  <span class="abs btn sub-btn">Sign Up</span>

  <div class="abs book" role="img" aria-label="Movers carrying boxes, darkened behind the booking panel"></div>
  <div class="abs book-panel"></div>
  <h2 class="abs book-title">Book an<br>Appointment</h2>
  <div class="abs book-sub">Moving Service</div>
  <div class="abs book-stat" style="left:769px"><div class="ic" style="background:var(--green)"><svg width="52" height="52" viewBox="0 0 52 52"><path d="M18 14h16M18 38h16M20 14c0 8 12 8 12 12s-12 4-12 12M32 14c0 8-12 8-12 12s12 4 12 12" fill="none" stroke="#fff" stroke-width="2.5"/></svg></div>1 hour</div>
  <div class="abs book-stat" style="left:888px"><div class="ic" style="background:var(--orange)"><svg width="52" height="52" viewBox="0 0 52 52"><circle cx="26" cy="26" r="13" fill="none" stroke="#fff" stroke-width="2.5"/><path d="M30 21c-1-2-8-2-8 1.5s8 2 8 6-7 3.5-8 1M26 16v20" fill="none" stroke="#fff" stroke-width="2"/></svg></div>$125.00</div>
  <span class="abs btn book-btn">Book Today</span>
</section>

<section>
  <div class="abs contact"></div>
  <div class="abs map" role="img" aria-label="Street map showing the office location"></div>
  <span class="abs map-btn">Get Directions</span>
  <h2 class="abs contact-title">Contact Us</h2>
  <div class="abs contact-item" style="top:2758px">
    <svg width="28" height="28" viewBox="0 0 28 28"><rect x="4" y="6" width="20" height="18" fill="none" stroke="#ccc" stroke-width="2"/><path d="M4 11h20M9 3v5M19 3v5" stroke="#ccc" stroke-width="2"/></svg>
    <div><h4>Schedule Your Move</h4><p>To arrange movers, please contact us at your convenience.&nbsp; We look forward to meeting you soon.</p></div>
  </div>
  <div class="abs contact-item" style="top:2850px">
    <svg width="28" height="28" viewBox="0 0 28 28"><path d="M14 3a8 8 0 0 0-8 8c0 6 8 14 8 14s8-8 8-14a8 8 0 0 0-8-8z" fill="none" stroke="#ccc" stroke-width="2"/><circle cx="14" cy="11" r="3" fill="#ccc"/></svg>
    <div><h4>Bolt Hauling LLC</h4><p>412 Linden Ave., Maple Grove, MS 39990, US</p></div>
  </div>
  <div class="abs contact-item" style="top:2920px">
    <svg width="28" height="28" viewBox="0 0 24 24"><path fill="#ccc" d="M6.6 10.8a15.1 15.1 0 0 0 6.6 6.6l2.2-2.2c.3-.3.7-.4 1-.2 1.1.4 2.3.6 3.6.6.6 0 1 .4 1 1V20c0 .6-.4 1-1 1A17 17 0 0 1 3 4c0-.6.4-1 1-1h3.5c.6 0 1 .4 1 1 0 1.3.2 2.5.6 3.6.1.3 0 .7-.2 1z"/></svg>
    <div><h4>(555) 014-2737</h4></div>
  </div>
  <div class="abs contact-item" style="top:2968px">
    <svg width="28" height="28" viewBox="0 0 28 28"><circle cx="14" cy="14" r="5" fill="none" stroke="#ccc" stroke-width="2"/><circle cx="14" cy="14" r="10" fill="none" stroke="#ccc" stroke-width="2" stroke-dasharray="4 3"/></svg>
    <div><h4>Service Area</h4><p>Central Mississippi</p></div>
  </div>
</section>

<footer>
  <div class="abs footer"></div>
  <div class="abs footer-copy">Copyright © 2017 Bolt Hauling LLC - All Rights Reserved.</div>
  <div class="abs footer-social"></div>
</footer>

</body>
</html>
```